'Bright Ledger Hidden Keys' Book Cover

I need a professional book cover design for my new upcoming book that shows people how to get a high credit score.

Here are my two websites:

https://www.moneywordbank-lexa.info
https://moneywordbank-lexa.com/

I am looking for a clean, professional design that pops (emotional touch) and separates from the other books that are on the market. Cover aspect ratio 1:4 for Pagewisp version and 1:5 for the paperback version. Yellow or blue are good colors - but not must. See the basic examples that I provided. File delivery format PDF.

Book Title: Bright Ledger Hidden Keys
Byline: The Quick Lift And Mend Manual for Stellar Borrowing

Currently on Brindlecart pre-order:
https://www.brindlecart.example/Bright-Ledger-Hidden-Keys-Stellar-ebook/dp/Q48MPLRT71

I am the author of 36 published books on Brindlecart. My author profile is here:
brindlecart.example/author/gideonvarly

Targeted audience: People that want to improve or repair their bad credit score.

Target Market(s)

People/consumers in the US that want to improve or repair their credit score.

Industry/Entity Type

Consumer

Font styles to use
Sans Serif

Colors

Designer to choose colors to be used in the design.

Requirements
Must have
• Author name, Title, byline, and graphic element(s).
Nice to have
• - 2020 edition logo / batch

```html
<!DOCTYPE html>
<html lang="en">
<head>
<meta charset="utf-8">
<title>Bright Ledger Hidden Keys — Book Cover</title>
<link rel="stylesheet" href="https://fonts.googleapis.com/css2?family=Bebas+Neue&family=Kumbh+Sans:wght@700&family=Oswald:wght@700&family=Cinzel:wght@600&display=swap">
<style>
  :root {
    --band: #6677b5;
    --aqua: #12fbff;
    --aqua-light: #c4ffff;
    --ink: #0a0a0a;
    --title-orange: #ea6b0a;
    --author-navy: #2f3a63;
    --gold-light: #ffd865;
    --gold-dark: #c8860e;
    --white: #ffffff;
  }
  html, body {
    margin: 0;
    padding: 0;
    width: 1200px;
    height: 855px;
    overflow: hidden;
    background: var(--aqua);
  }
  .cover {
    position: relative;
    width: 1200px;
    height: 855px;
  }
  .cover-art {
    position: absolute;
    inset: 0;
  }
  .back-blurb {
    position: absolute;
    left: 68px;
    top: 202px;
    width: 440px;
    margin: 0;
    font-family: 'Kumbh Sans', sans-serif;
    font-weight: 700;
    font-size: 22.5px;
    line-height: 28.5px;
    color: var(--ink);
    text-align: center;
  }
  .back-blurb p { margin: 0 0 28.5px; }
  .title-font { font-family: 'Bebas Neue', sans-serif; }
  .spine-font { font-family: 'Oswald', sans-serif; font-weight: 700; }
  .subtitle-font { font-family: 'Kumbh Sans', sans-serif; font-weight: 700; }
  .badge-font { font-family: 'Cinzel', serif; font-weight: 600; }
</style>
</head>
<body>
<div class="cover">
  <svg class="cover-art" width="1200" height="855" viewBox="0 0 1200 855" xmlns="http://www.w3.org/2000/svg">
    <defs>
      <linearGradient id="front-wash" x1="0" y1="0" x2="1" y2="0">
        <stop offset="0" stop-color="#5ff9ff"/>
        <stop offset="1" stop-color="#c9ffff"/>
      </linearGradient>
      <linearGradient id="hand-card-tones" x1="0" y1="0" x2="1" y2="0.3">
        <stop offset="0" stop-color="#f0c39c"/>
        <stop offset="0.35" stop-color="#d9a27c"/>
        <stop offset="0.55" stop-color="#2a2d5e"/>
        <stop offset="1" stop-color="#14163a"/>
      </linearGradient>
      <radialGradient id="gold" cx="0.4" cy="0.35" r="0.7">
        <stop offset="0" stop-color="var(--gold-light)"/>
        <stop offset="1" stop-color="var(--gold-dark)"/>
      </radialGradient>
    </defs>

    <!-- background bands -->
    <rect class="band band-top" x="0" y="0" width="1200" height="32" fill="var(--band)"/>
    <rect class="back-field" x="0" y="32" width="1200" height="614" fill="var(--aqua)"/>
    <rect class="front-field" x="630" y="32" width="570" height="614" fill="url(#front-wash)"/>
    <rect class="band band-middle" x="0" y="646" width="1200" height="100" fill="var(--band)"/>
    <rect class="bottom-field" x="0" y="746" width="1200" height="109" fill="var(--aqua)"/>
    <rect class="front-bottom-field" x="630" y="746" width="570" height="109" fill="url(#front-wash)"/>

    <!-- barcode placeholder -->
    <rect class="barcode-box" x="355" y="716" width="192" height="114" fill="var(--white)"/>

    <!-- spine -->
    <g class="spine" transform="translate(587 70) rotate(90)">
      <text class="spine-font spine-title" x="0" y="0" font-size="30" fill="var(--ink)" textLength="310" lengthAdjust="spacingAndGlyphs">BRIGHT LEDGER HIDDEN KEYS</text>
      <text class="spine-font spine-author" x="374" y="0" font-size="30" fill="var(--ink)" textLength="172" lengthAdjust="spacingAndGlyphs">GIDEON VARLY</text>
    </g>

    <!-- front subtitle -->
    <text class="subtitle-font front-subtitle" text-anchor="middle" font-size="21" fill="var(--ink)">
      <tspan x="914" y="86">THE QUICK LIFT AND MEND MANUAL</tspan>
      <tspan x="914" y="115">FOR STELLAR BORROWING</tspan>
    </text>

    <!-- hero image area -->
    <rect class="hero-image" x="630" y="134" width="532" height="262" rx="6" fill="url(#hand-card-tones)" role="img" aria-label="Photo of a hand holding out a dark blue credit card"/>

    <!-- title -->
    <text class="title-font title-line-1" x="648" y="501" font-size="150" fill="var(--title-orange)" textLength="524" lengthAdjust="spacingAndGlyphs">BRIGHT LEDGER</text>
    <text class="title-font title-line-2" x="648" y="619" font-size="160" fill="var(--ink)" textLength="520" lengthAdjust="spacingAndGlyphs">HIDDEN KEYS</text>

    <!-- edition badge -->
    <g class="edition-badge">
      <circle cx="1100" cy="693" r="57" fill="#8a5a10" opacity="0.35"/>
      <circle cx="1097" cy="690" r="56" fill="url(#gold)"/>
      <circle cx="1097" cy="690" r="44" fill="none" stroke="#a8700c" stroke-width="1.5"/>
      <text class="badge-font" x="1097" y="687" text-anchor="middle" font-size="21" fill="#3a2a08">2020</text>
      <text class="badge-font" x="1097" y="706" text-anchor="middle" font-size="11" fill="#3a2a08">EDITION</text>
    </g>

    <!-- front author -->
    <text class="title-font front-author" x="742" y="830" font-size="68" fill="var(--author-navy)" textLength="340" lengthAdjust="spacingAndGlyphs">GIDEON VARLY</text>
  </svg>

  <div class="back-blurb">
    <p>Did you know that 82% of financial problems are due to lack of credit card knowledge? With over 75 million people in the United States in need of credit improvement or repair, one of the largest issues is the lack of credit know-how.</p>
    <p>A good credit score is essential if you want to enjoy financial freedom.</p>
  </div>
</div>
</body>
</html>
```